Bramble Artisan Wood Fired Pizza business card design

I have a logo and need an eye catching design that will get me noticed.
My business is wood fired pizza. I want a bold design that will make our customers remember us and the food that we serve. Work with the colors of our logo and texts. Maybe add designs that lend to what or how pizza is made using our wood fired oven?

Target Market(s)

Foodies!

Contact Information for Business Card

Bramble Artisan Wood Fired Pizza
Our slogan is Fast. Fresh. Handcrafted
Catering for all events

Requirements
Must have
• Noel Pruett
Telephone 570 555 0187
website www.trybramble.com
Facebook @trybramblepizza maybe use the facebook logo next to it
Instagram trybramblepizza maybe use the instagram logo next to it
Catering for all events
Nice to have
• Maybe pizza peels, pizza cutters? Wood? Fired wood? Using our flame in the background?
Please work with different colored text so each sentence stands out? A themed color for facebook?
Maybe work with the colors within our logo?
Please try to use the our bramble font, but not a must have.

```html
<!DOCTYPE html>
<html lang="en">
<head>
<meta charset="utf-8">
<title>Bramble Artisan Wood Fired Pizza – Business Card</title>
<link rel="stylesheet" href="https://fonts.googleapis.com/css2?family=Roboto:wght@400;700;900&display=swap">
<style>
  :root {
    --stage: #2e2f31;
    --orange: #f28c1a;
    --orange-deep: #e9791a;
    --red: #cc1417;
    --char: #2b2b2c;
    --white: #ffffff;
  }
  * { box-sizing: border-box; margin: 0; padding: 0; }
  html, body { width: 1200px; height: 900px; overflow: hidden; }
  body {
    background: var(--stage);
    font-family: "Roboto", Arial, sans-serif;
    position: relative;
  }
  .card {
    position: absolute;
    left: 250px;
    width: 700px;
    height: 400px;
    background: linear-gradient(135deg, var(--orange) 0%, var(--orange-deep) 100%);
    overflow: hidden;
    box-shadow: 0 10px 24px rgba(0,0,0,.45);
  }
  .card-front { top: 40px; }
  .card-back { top: 470px; }

  /* front */
  .front-brand {
    position: absolute;
    top: 92px; left: 0; right: 0;
    text-align: center;
    color: var(--white);
  }
  .brand-line {
    font-size: 14px; font-weight: 700; letter-spacing: 4px;
  }
  .brand-name {
    font-size: 62px; font-weight: 900; letter-spacing: 8px; line-height: 1.05;
  }
  .brand-est { font-size: 10px; font-weight: 700; letter-spacing: 2px; }
  .slogan {
    margin-top: 12px;
    font-size: 16px; color: var(--red); font-weight: 400;
  }
  .front-band {
    position: absolute; left: 0; right: 0; top: 278px; height: 26px;
    background: var(--red);
  }
  .catering {
    position: absolute; left: 0; right: 0; top: 318px;
    text-align: center;
    font-size: 17px; font-weight: 700; letter-spacing: 1px;
    color: var(--red);
  }
  .front-foot {
    position: absolute; right: 0; bottom: 0; width: 110px; height: 30px;
    background: var(--white);
  }
  .front-foot-dot {
    position: absolute; right: 72px; bottom: 7px;
    width: 16px; height: 16px; border-radius: 50%; background: var(--char);
  }

  /* back */
  .flame-art { position: absolute; right: 0; top: 0; width: 460px; height: 400px; }
  .back-brand {
    position: absolute; left: 36px; top: 44px; color: var(--white);
  }
  .back-brand .brand-name { font-size: 54px; letter-spacing: 7px; }
  .person { position: absolute; left: 36px; top: 180px; }
  .person-name {
    font-size: 24px; font-weight: 700; color: var(--red); letter-spacing: .5px;
  }
  .person-role { font-size: 17px; color: var(--white); margin-top: 2px; }
  .contact {
    position: absolute; left: 36px; top: 262px;
    list-style: none;
  }
  .contact li {
    display: flex; align-items: center; gap: 10px;
    font-size: 17px; color: var(--white); line-height: 24px;
  }
  .contact svg { width: 14px; height: 14px; fill: var(--red); flex: none; }
  .social-dot {
    width: 14px; height: 14px; border-radius: 50%; background: var(--red); flex: none;
  }
</style>
</head>
<body>

<section class="card card-front">
  <div class="front-brand">
    <div class="brand-line">ARTISAN WOOD FIRED PIZZA</div>
    <div class="brand-name">BRAMBLE</div>
    <div class="brand-est">EST. 2020</div>
    <div class="slogan">Fast. Fresh. Handcrafted</div>
  </div>
  <div class="front-band"></div>
  <div class="catering">CATERING FOR ALL EVENTS</div>
  <div class="front-foot"><span class="front-foot-dot"></span></div>
</section>

<section class="card card-back">
  <svg class="flame-art" viewBox="0 0 460 400" role="img" aria-label="Large flame artwork in red and charcoal">
    <defs>
      <linearGradient id="flameFill" x1="0" y1="0" x2="1" y2="1">
        <stop offset="0" stop-color="#cc1417"/>
        <stop offset="1" stop-color="#2b2b2c"/>
      </linearGradient>
    </defs>
    <path d="M140 400 C40 330 60 210 170 150 C250 105 270 60 330 20 L460 20 L460 400 Z" fill="url(#flameFill)"/>
  </svg>

  <div class="back-brand">
    <div class="brand-line">ARTISAN WOOD FIRED PIZZA</div>
    <div class="brand-name">BRAMBLE</div>
    <div class="brand-est">EST. 2020</div>
  </div>

  <div class="person">
    <div class="person-name">NOEL PRUETT</div>
    <div class="person-role">Owner/Pizzaiolo</div>
  </div>

  <ul class="contact">
    <li>
      <svg viewBox="0 0 24 24"><path d="M6.6 10.8a15 15 0 0 0 6.6 6.6l2.2-2.2a1 1 0 0 1 1-.25 11.4 11.4 0 0 0 3.6.57 1 1 0 0 1 1 1V20a1 1 0 0 1-1 1A17 17 0 0 1 3 4a1 1 0 0 1 1-1h3.5a1 1 0 0 1 1 1c0 1.25.2 2.45.57 3.6a1 1 0 0 1-.25 1z"/></svg>
      570 555 0187
    </li>
    <li>
      <svg viewBox="0 0 24 24"><path d="M2 5h20v14H2z M2 5l10 8 10-8" fill="none" stroke="#cc1417" stroke-width="2.5"/></svg>
      hello@trybramble.com
    </li>
    <li>
      <svg viewBox="0 0 24 24"><circle cx="12" cy="12" r="9" fill="none" stroke="#cc1417" stroke-width="2.5"/><path d="M3 12h18M12 3c3 3 3 15 0 18M12 3c-3 3-3 15 0 18" fill="none" stroke="#cc1417" stroke-width="2"/></svg>
      www.trybramble.com
    </li>
    <li><span class="social-dot"></span>/trybramblepizza</li>
    <li><span class="social-dot"></span>@trybramblepizza</li>
  </ul>
</section>

</body>
</html>
```